need a clean, modern job advertisement designed for social media (Facebook & Instagram).

The post is to advertise two positions:
• Leading Hand Boilermaker
• Dragline Fitter
We want the design to match our KRT Field Maintenance branding: blue, white, strong, professional, mining-industry style.
What the design should include:
Bold headline: “WE’RE HIRING”
Sub-headline: “Leading Hand Boilermaker & Dragline Fitter”
Key points:
• Bowen Basin based
• Dragline & shovel maintenance
• Great pay + long-term work
• Locally owned & operated
KRT logo placed cleanly
Space for 1–2 images (boilermaking or dragline work)
Design style:
Strong and industrial
Blue/white colour scheme
Easy to read at a glance
Suitable for a square 1080×1080 design

```html
<!DOCTYPE html>
<html lang="en">
<head>
<meta charset="utf-8">
<title>KRT Field Maintenance – We're Hiring</title>
<link rel="stylesheet" href="https://fonts.googleapis.com/css2?family=Anton&family=Montserrat:wght@600;700;800&display=swap">
<style>
  :root {
    --blue: #3aa6e0;
    --blue-light: #6cc4f0;
    --ink: #0b0b0c;
    --charcoal: #1f2022;
    --white: #ffffff;
    --paper: #f3f4f5;
    --text-dark: #1b1c1e;
    --stage: #a6a6a6;
  }
  * { margin: 0; padding: 0; box-sizing: border-box; }
  html, body {
    width: 1200px; height: 1117px; overflow: hidden;
    background: var(--stage);
  }
  .post {
    position: absolute; left: 41px; top: 0;
    width: 1117px; height: 1117px; overflow: hidden;
    background: var(--paper);
    font-family: "Montserrat", Arial, sans-serif;
  }
  .post-shapes { position: absolute; inset: 0; }
  .headline {
    position: absolute; left: 0; top: 68px; width: 100%;
    text-align: center;
    font-family: "Anton", "Impact", sans-serif;
    font-size: 172px; line-height: 1; letter-spacing: -1px;
    color: var(--white);
  }
  .headline .accent { color: var(--blue); }
  .subheadline {
    position: absolute; left: 0; top: 254px; width: 100%;
    text-align: center;
    font-weight: 600; font-size: 46px; line-height: 52px;
    color: var(--white);
    padding-left: 0;
    transform: translateX(-2px);
  }
  .benefits {
    position: absolute; left: 98px; top: 730px;
    list-style: none;
  }
  .benefits li {
    display: flex; align-items: center;
    height: 54px;
    font-weight: 700; font-size: 30px; letter-spacing: 0.2px;
    color: var(--text-dark);
  }
  .benefits .tick { width: 28px; height: 28px; margin-right: 21px; flex: none; }
  .brand {
    position: absolute; left: 728px; top: 820px; width: 370px;
    display: flex; align-items: center; justify-content: center; gap: 14px;
    font-weight: 800; font-size: 34px; line-height: 38px;
    color: var(--charcoal);
  }
  .brand .brand-dot {
    width: 22px; height: 22px; border-radius: 50%;
    background: var(--blue); flex: none;
  }
  .website {
    position: absolute; left: 98px; top: 1024px;
    display: flex; align-items: center; gap: 22px;
    font-weight: 600; font-size: 40px; color: var(--white);
  }
  .website svg { width: 34px; height: 34px; }
</style>
</head>
<body>
<main class="post">
  <svg class="post-shapes" viewBox="0 0 1117 1117" xmlns="http://www.w3.org/2000/svg">
    <defs>
      <linearGradient id="topGrad" x1="0" y1="0" x2="0" y2="1">
        <stop offset="0" stop-color="#3a3b3d"/>
        <stop offset="1" stop-color="#0c0c0d"/>
      </linearGradient>
      <linearGradient id="paperGrad" x1="0" y1="0" x2="0" y2="1">
        <stop offset="0" stop-color="#e9eaec"/>
        <stop offset="1" stop-color="#ffffff"/>
      </linearGradient>
      <linearGradient id="photo1" x1="0" y1="0" x2="1" y2="1">
        <stop offset="0" stop-color="#c9ccd0"/>
        <stop offset="0.6" stop-color="#7d6f60"/>
        <stop offset="1" stop-color="#3b3834"/>
      </linearGradient>
      <linearGradient id="photo2" x1="0" y1="0" x2="1" y2="1">
        <stop offset="0" stop-color="#1d2438"/>
        <stop offset="0.5" stop-color="#3a4a7a"/>
        <stop offset="1" stop-color="#0d1020"/>
      </linearGradient>
      <linearGradient id="photo3" x1="0" y1="0" x2="1" y2="1">
        <stop offset="0" stop-color="#2a5a5c"/>
        <stop offset="0.6" stop-color="#3d2e3a"/>
        <stop offset="1" stop-color="#1a1618"/>
      </linearGradient>
    </defs>

    <!-- upper dark background -->
    <g role="img" aria-label="Background photo: field service ute and mine site in black and white">
      <rect x="0" y="0" width="1117" height="620" fill="url(#topGrad)"/>
    </g>

    <!-- lower light area -->
    <polygon points="0,520 1117,640 1117,1117 0,1117" fill="url(#paperGrad)"/>

    <!-- blue accent stripes -->
    <polygon points="0,426 115,438 108,468 0,456" fill="var(--blue)"/>
    <polygon points="0,456 108,468 100,490 0,478" fill="#e2e4e6"/>
    <polygon points="1010,570 1117,580 1117,610 1004,600" fill="var(--blue)"/>

    <!-- photo panels -->
    <g>
      <polygon points="106,392 425,392 358,682 46,682" fill="var(--white)"/>
      <polygon points="116,400 414,400 351,674 57,674" fill="url(#photo1)" role="img" aria-label="Photo: crew in hi-vis rigging a dragline boom"/>
    </g>
    <g>
      <polygon points="430,392 742,392 674,682 366,682" fill="var(--white)"/>
      <polygon points="440,400 731,400 667,674 377,674" fill="url(#photo2)" role="img" aria-label="Photo: boilermaker welding at night"/>
    </g>
    <g>
      <polygon points="745,392 1062,392 994,682 686,682" fill="var(--white)"/>
      <polygon points="755,400 1051,400 987,674 697,674" fill="url(#photo3)" role="img" aria-label="Photo: cutting torch on a dragline structure"/>
    </g>

    <!-- footer band -->
    <polygon points="0,982 722,982 745,1062 1117,1062 1117,1117 0,1117" fill="var(--ink)"/>
    <polygon points="745,1062 1117,1062 1117,1083 751,1083" fill="var(--blue)"/>
    <rect x="0" y="1083" width="1117" height="34" fill="var(--ink)"/>
  </svg>

  <h1 class="headline">WE’RE <span class="accent">HIRING</span></h1>
  <p class="subheadline">LEADING HAND BOILERMAKER<br>&amp; DRAGLINE FITTER</p>

  <ul class="benefits">
    <li><svg class="tick" viewBox="0 0 28 28"><circle cx="14" cy="14" r="13" fill="#3aa6e0"/><path d="M8 14.5l4 4 8-8.5" fill="none" stroke="#fff" stroke-width="3" stroke-linecap="round" stroke-linejoin="round"/></svg>BOWEN BASIN BASED</li>
    <li><svg class="tick" viewBox="0 0 28 28"><circle cx="14" cy="14" r="13" fill="#3aa6e0"/><path d="M8 14.5l4 4 8-8.5" fill="none" stroke="#fff" stroke-width="3" stroke-linecap="round" stroke-linejoin="round"/></svg>DRAGLINE &amp; SHOVEL MAINTENANCE</li>
    <li><svg class="tick" viewBox="0 0 28 28"><circle cx="14" cy="14" r="13" fill="#3aa6e0"/><path d="M8 14.5l4 4 8-8.5" fill="none" stroke="#fff" stroke-width="3" stroke-linecap="round" stroke-linejoin="round"/></svg>GREAT PAY + LONG-TERM WORK</li>
    <li><svg class="tick" viewBox="0 0 28 28"><circle cx="14" cy="14" r="13" fill="#3aa6e0"/><path d="M8 14.5l4 4 8-8.5" fill="none" stroke="#fff" stroke-width="3" stroke-linecap="round" stroke-linejoin="round"/></svg>LOCALLY OWNED &amp; OPERATED</li>
  </ul>

  <div class="brand"><span class="brand-dot"></span><span>KRT Field<br>Maintenance</span></div>

  <div class="website">
    <svg viewBox="0 0 34 34"><circle cx="17" cy="17" r="16" fill="#3aa6e0"/><g fill="none" stroke="#0b0b0c" stroke-width="1.8"><circle cx="17" cy="17" r="9"/><ellipse cx="17" cy="17" rx="4" ry="9"/><line x1="8" y1="17" x2="26" y2="17"/><line x1="9.5" y1="12.5" x2="24.5" y2="12.5"/><line x1="9.5" y1="21.5" x2="24.5" y2="21.5"/></g></svg>
    <span>krtfieldmaintenance.com</span>
  </div>
</main>
</body>
</html>
```